Automotive Accessories Business Card

Design a business template that match our new logo design and our industry.

https://www.kelvorauto.com/

Target Market(s)

Aftermarket auto parts and accessories

Industry/Entity Type

automotive

Contact Information for Business Card

company logo

Font styles to use
Serif
Sans Serif

Colors
EB3D1F
EC4F4E
F09395
F8D3D4
FCEDEE

```html
<!DOCTYPE html>
<html lang="en">
<head>
<meta charset="utf-8">
<title>Kelvor Auto Parts – Business Card</title>
<link rel="stylesheet" href="https://fonts.googleapis.com/css2?family=Exo+2:wght@400;500;700&display=swap">
<style>
  :root {
    --red: #d61f26;
    --charcoal: #3d3d3f;
    --white: #ffffff;
    --backdrop: #dadada;
    --band-dark: #3d3d3f;
    --band-red: #d61f26;
  }
  * { box-sizing: border-box; margin: 0; padding: 0; }
  html, body {
    width: 1055px; height: 1200px; overflow: hidden;
    background: var(--backdrop);
    font-family: "Exo 2", sans-serif;
  }
  .canvas { position: relative; width: 1055px; height: 1200px; }
  .card {
    position: absolute; left: 107px; width: 840px; height: 480px;
    overflow: hidden; box-shadow: 0 6px 18px rgba(0,0,0,.18);
  }
  .card--front { top: 80px; background: var(--white); }
  .card--back { top: 640px; background: var(--red); }
  .card__panel { position: absolute; inset: 0; width: 840px; height: 480px; }
  .racing-band {
    position: absolute; left: 0; bottom: 0; width: 100%; height: 57px;
    background: linear-gradient(180deg, var(--white) 0 10%, var(--band-dark) 10% 50%, var(--band-red) 50% 90%, var(--white) 90%);
    opacity: .9;
  }
  .brand {
    position: absolute; display: flex; align-items: center; gap: 12px;
    font-weight: 700; letter-spacing: 2px; white-space: nowrap;
  }
  .brand__mark { width: 22px; height: 22px; }
  .card--front .brand { left: 56px; top: 186px; font-size: 40px; color: var(--red); }
  .card--front .brand__mark { background: var(--charcoal); }
  .card--back .brand { left: 50%; top: 190px; transform: translateX(-50%); font-size: 56px; color: var(--white); }
  .card--back .brand__mark { width: 30px; height: 30px; background: var(--white); }
  .holder { position: absolute; left: 480px; top: 88px; color: var(--white); }
  .holder__name { font-size: 32px; font-weight: 700; letter-spacing: .5px; line-height: 1; }
  .holder__role { font-size: 20px; font-weight: 500; margin-top: 8px; }
  .contact { position: absolute; display: flex; align-items: center; color: var(--white); }
  .contact__icon {
    width: 56px; height: 46px; background: var(--white);
    clip-path: polygon(8% 0, 100% 0, 92% 100%, 0 100%);
    display: flex; align-items: center; justify-content: center;
  }
  .contact__icon svg { width: 22px; height: 22px; fill: var(--charcoal); }
  .contact--address { left: 413px; top: 198px; }
  .contact--address .contact__text { margin-left: 22px; font-size: 20px; font-weight: 500; line-height: 1.35; }
  .contact--phone { left: 403px; top: 288px; }
  .contact--phone .contact__text { margin-left: 20px; font-size: 28px; font-weight: 500; }
</style>
</head>
<body>
<main class="canvas">
  <section class="card card--front" aria-label="Business card front">
    <svg class="card__panel" viewBox="0 0 840 480" aria-hidden="true">
      <polygon points="463,0 840,0 840,423 406,423" fill="var(--charcoal)"/>
      <polygon points="478,0 840,0 840,423 421,423" fill="var(--red)"/>
    </svg>
    <div class="brand"><span class="brand__mark"></span>KELVOR AUTO</div>
    <div class="holder">
      <p class="holder__name">MARCUS DALTON</p>
      <p class="holder__role">Owner</p>
    </div>
    <div class="contact contact--address">
      <span class="contact__icon"><svg viewBox="0 0 24 24"><path d="M12 2a7 7 0 0 0-7 7c0 5 7 13 7 13s7-8 7-13a7 7 0 0 0-7-7zm0 9.5A2.5 2.5 0 1 1 12 6.5a2.5 2.5 0 0 1 0 5z"/></svg></span>
      <p class="contact__text">482 W. Cedar St. Unit B<br>Linwood, CA, 92408</p>
    </div>
    <div class="contact contact--phone">
      <span class="contact__icon"><svg viewBox="0 0 24 24"><path d="M6.6 10.8a15 15 0 0 0 6.6 6.6l2.2-2.2a1 1 0 0 1 1-.25 11.4 11.4 0 0 0 3.6.57 1 1 0 0 1 1 1V20a1 1 0 0 1-1 1A17 17 0 0 1 3 4a1 1 0 0 1 1-1h3.5a1 1 0 0 1 1 1c0 1.25.2 2.45.57 3.57a1 1 0 0 1-.25 1z"/></svg></span>
      <p class="contact__text">866-555-0142</p>
    </div>
    <div class="racing-band" role="img" aria-label="Checkered racing flag band in charcoal, red and white"></div>
  </section>

  <section class="card card--back" aria-label="Business card back">
    <div class="brand"><span class="brand__mark"></span>KELVOR AUTO</div>
    <div class="racing-band" role="img" aria-label="Checkered racing flag band in charcoal, red and white"></div>
  </section>
</main>
</body>
</html>
```